Business cards for start-up accounting firm

I'm looking for a double sided business card ready for upload into Prontel ink or similar print providers with no modification required by me.
I'm looking for something simple as i think cards that are too 'busy' actually detract from the message. I have some thoughts but more than happy to see what comes up. The logo i have came out of left field and i love it the moment i saw it!

My thoughts:

Side 1: Just the logo, perhaps on a dark grey or charcoal background to make the logo colours stand out?

Side 2: The call to action from me website 'Looking for a more relaxed, friendly and interactive relationship with your accountant?' with my contact information
Name: Gavin Ormsby
Email: gavin@quellorix.com.au
Website: www.quellorix.com.au
Phone: 1300 742 916

The call to action needs to be the first thing they see when they look at side 2. If it helps to know what we do and how we do it there is a draft website at www.quellorix.com.au

Like i said, happy to consider anything that comes up :)

Target Market(s)

i'm targeting small business owners who experience a lot of stress around finacial reporting and have had bad experiences with accountants in the past.

Industry/Entity Type

Accounting

Contact Information for Business Card

Contained in the Description

Font styles to use
Serif
Sans Serif
Other font styles liked:
• See logo files attached

Colors
474747

Requirements
Must have
• My logo, slogan and contact information

```html
<!DOCTYPE html>
<html lang="en">
<head>
<meta charset="utf-8">
<title>Quellorix Business Card</title>
<link href="https://fonts.googleapis.com/css2?family=Signika:wght@400;600;700&display=swap" rel="stylesheet">
<style>
  :root {
    --backdrop: #9c9c9c;
    --card-white: #f7f6f3;
    --card-black: #0c0c0c;
    --brand-purple: #8c3787;
    --brand-purple-light: #9d4697;
    --brand-yellow: #f1d01c;
    --text-white: #ffffff;
    --watermark: rgba(140, 55, 135, 0.07);
  }
  * { box-sizing: border-box; margin: 0; padding: 0; }
  html, body {
    width: 1200px; height: 800px; overflow: hidden;
    background: var(--backdrop);
    font-family: "Signika", sans-serif;
  }
  .stage {
    position: relative; width: 1200px; height: 800px;
    display: flex; align-items: center; justify-content: center; gap: 40px;
  }
  .card {
    position: relative; width: 540px; height: 309px; overflow: hidden;
    box-shadow: 0 6px 18px rgba(0,0,0,0.25);
  }
  /* Front side */
  .card-front { background: var(--card-white); }
  .watermark-name {
    position: absolute; left: 26px; top: 70px;
    font-weight: 700; font-size: 64px; letter-spacing: 1px;
    color: var(--watermark);
  }
  .brand-name {
    position: absolute; right: 34px; top: 44px;
    display: flex; align-items: center; gap: 8px;
    font-weight: 700; font-size: 40px; color: var(--brand-purple);
  }
  .brand-dot {
    width: 14px; height: 14px; border-radius: 50%; background: var(--brand-yellow);
  }
  .person-name {
    position: absolute; left: 42px; top: 162px;
    font-weight: 600; font-size: 24px; color: var(--brand-purple);
  }
  .rule {
    position: absolute; left: 28px; right: 0; top: 196px;
    height: 3px; background: var(--brand-yellow);
  }
  .contact-band {
    position: absolute; left: 0; right: 0; top: 203px; bottom: 0;
    background: linear-gradient(90deg, var(--brand-purple), var(--brand-purple-light) 45%, var(--brand-purple));
    color: var(--text-white); font-size: 15px;
  }
  .contact-item { position: absolute; display: flex; align-items: center; gap: 12px; }
  .contact-item svg { width: 16px; height: 16px; flex: none; }
  .contact-phone { left: 42px; top: 26px; }
  .contact-email { left: 42px; top: 60px; }
  .contact-web { right: 30px; top: 26px; }
  /* Back side */
  .card-back {
    background: var(--card-black);
    display: flex; align-items: center; justify-content: center;
  }
  .card-back .brand-name { position: static; font-size: 56px; gap: 12px; }
  .card-back .brand-dot { width: 18px; height: 18px; }
</style>
</head>
<body>
<main class="stage">
  <section class="card card-front" aria-label="Card front">
    <div class="watermark-name" aria-hidden="true">Quellorix</div>
    <div class="brand-name"><span class="brand-dot"></span>Quellorix</div>
    <p class="person-name">Gavin Ormsby</p>
    <div class="rule"></div>
    <div class="contact-band">
      <div class="contact-item contact-phone">
        <svg viewBox="0 0 16 16" aria-hidden="true"><path fill="#f1d01c" d="M3 1.5l3 .5 1 3.2-1.8 1.3a8 8 0 004.3 4.3l1.3-1.8 3.2 1 .5 3-2 1.5C6.8 14.5 1.5 9.2 1.5 3.5z"/></svg>
        <span>1300 742 916</span>
      </div>
      <div class="contact-item contact-email">
        <svg viewBox="0 0 16 16" aria-hidden="true"><rect x="1" y="3.5" width="14" height="10" rx="1" fill="#f1d01c"/><path d="M1.5 4.5l6.5 5 6.5-5" fill="none" stroke="#8c3787" stroke-width="1.4"/></svg>
        <span>gavin@quellorix.com.au</span>
      </div>
      <div class="contact-item contact-web">
        <svg viewBox="0 0 16 16" aria-hidden="true"><circle cx="8" cy="8" r="7" fill="#f1d01c"/><ellipse cx="8" cy="8" rx="3" ry="7" fill="none" stroke="#8c3787" stroke-width="1.1"/><path d="M1 8h14" stroke="#8c3787" stroke-width="1.1"/></svg>
        <span>www.quellorix.com.au</span>
      </div>
    </div>
  </section>
  <section class="card card-back" aria-label="Card back">
    <div class="brand-name"><span class="brand-dot"></span>Quellorix</div>
  </section>
</main>
</body>
</html>
```